Menu Design

I am seeking a designer to re create our menu for our stores.

I have attached our current menu and would I have also attached some menus I like for inspiration

The menu is to be split across 2 pages, Please present the menu of 2 horizontal a4 pages and our in house designer will adjust the final PSD file to suit our stores different configurations.

Kindest Regards

The text for the menu is as follows

BASE SHAKE (Choc, Strawberry, Vanilla, Banana) (Reg $4.95 Large $5.95)

ADD-ON'S

Protein $2
Superfruit $2
Coconut Water $2
Chia Seeds $1
Energiser $1
Fat-burner $1
L-Carnitine $1
Glutamine $1

ACTIVE LIFESTYLE SMOOTHIES (Available in Chocolate, Strawberry, Vanilla, Banana) (Reg $6.95 Large $7.95)

Kick Start (Muscle, Weight Loss)
Protein, Protein Frozen Yoghurt, Caffeine, Water, Ice

Recovery (Muscle, Weight Loss)
Protein, Protein Frozen Yoghurt, L-Glutamine, Viamin C Powder, Water, Ice

Shredder (Weight Loss)
Protein, Protein Frozen Yoghurt, L-Carnitine, Thermogenic, Vitamin C Powder, Chia Seeds, Water, Ice

Muscle Maker (Muscle)
Protein, Protein Frozen Yoghurt, Full Cream Milk, Dextrose, Flaxseed Oil, Creatine Monohydrate

SUPER SMOOTHIES (Reg $8.95 Large $9.95)

Honey Nutter (Favourite, Muscle, Weight Loss)
Chocolate Protein, Natural Peanut Butter, Chia Seeds, Manuka Honey, Cocoa Nibs, Water, Ice

Choc-Mint Powerhouse (Muscle, Weight Loss)
Chocolate Protein, Mint, Natural Peanut Butter, Walnuts, Almonds, Chia Seeds, Manuka Honey, Water, Ice

Forever Energy (Favourite, Muscle, Weight Loss, Vitality)
Vanilla Protein, Almond Flakes, Avocado, Chia Seeds, Banana, Dates, Cacao Nibs, Acai Powder, Coconut Water, Ice

Cardio Berry- Bomb (Muscle, Weight Loss)
Vanilla Protein, Banana, Mixed Berries, Chia Seeds, Antioxidant Mix (pomegranate, maqui, acai, elderflower, green tea powder), Coconut Water, Ice\

Toxin Cleanser (Muscle, Weight Loss, Vitality)
Vanilla Protein, Kale, Pear, Banana, Pineapple, Chia Seeds, Water, Ice

Morning Glory (Muscle, Weight Loss, Vitality)
Vanilla Protein, Blueberries, Goji Berries, Walnuts, Manuka Honey, Avocado, Coconut Water, Ice

SUPERFRUIT SMOOTHIES (Reg $8.95 Large $9.95)

Tropical Tonic (Muscle, Weight Loss, Vitality)
Vanilla Protein, Passionfruit, Almonds, Mango, Avocado, Manuka Honey, Chia Seeds, Coconut Water, Ice

Peach Pick-Me-Up (Muscle, Weight Loss, Vitality)
Vanilla Protein, Peach, Banana, Kale, Pear, Almonds, Chia Seeds, Coconut Water, Ice

Mango Madness (Favourite, Muscle, Weight Loss, Vitality)
Vanilla Protein, Mango, Almond Flakes, Manuka Honey, Ice, Chia Seeds, Water, Ice

Banana Bliss (Favourite, Muscle, Weight Loss)
Banana Protein, Banana, Cacao Nibs, Manuka Honey, Chia Seeds, Walnuts, Cinnamon, Chia Seeds, Water, Ice

Berry Sweet (Favourite, Muscle, Weight Loss)
Strawberry Protein, Mixed Berries, Acai Powder, Goji Berries, Cranberries, Shredded Coconut, Water, Ice

VEGAN SMOOTHIES (Reg $8.95 Large $9.95)

Acai (Vitality, Weight Loss, Dairy Free, Gluten Free)
Acai Powder, Banana, Chia Seeds, Goji Berries, Cranberries, Coconut Water, Ice

Energiser (Vitality, Weight Loss, Dairy Free, Gluten Free)
Raw Energy Powder (traditional herbs, slow-release ancient seeds, and concentrated sea minerals), Acai Powder, Blueberries, Avocado, Chia Seeds, Coconut Water, Ice

Complete Biotic (Vitality, Weight Loss, Dairy Free, Gluten Free)
Raw Pre-Probiotic Powder, Mango, Chia Seeds, Almond Flakes, Coconut Water, Ice

Vegan Vigor (Favourite, Muscle, Weight Loss, Vitality, Dairy Free, Gluten Free)
Vegetable Protein, Blueberries, Banana, Cinnamon, Walnuts, Chia Seeds, Antioxidant Mix (pomegranate, maqui, acai, elderflower, green tea powder), Coconut Water, Ice

KIDS ($3.95)

Chocolate
Low Fat Milk, Cacao Nibs, Chia Seeds

Strawberry
Low Fat Milk, Strawberries, Goji Berries

Banana
Low Fat Milk, Banana, Chia Seeds

Banana Choc
Low Fat Milk, Banana, Honey, Cacao Nibs

FROZEN YOGHURT (Up to 3 toppings- extra toppings $0.50 each)

Small $4.50
Medium $6.00
Large $7.50

PROTEIN PANCAKES (Available in Chocolate, Strawberry, Banana)

3 Stack $6.95
5 Stack $8.45
Protein Pocket $3.50

FOOD AND EXTRA'S

Acai Bowl $9.95
Protein Balls $2
Vantor Bars $4.50

Lumo- Leaf Tea $3.95
Bottled Water $2.45
Coconut Water $3.30

Target Market(s)

Our customers are both male and female 18 - 35 who have an interest in health, fitness, healthy eating and overall well being

Industry/Entity Type

House

Colors
0492cd
e567a6
ebf7f9
33a6d7
b768aa

Requirements
Must have
• must be clean and easy to read.
Nice to have
• Images of the shakes taken from the uploaded psd file

```html
<!DOCTYPE html>
<html lang="en">
<head>
<meta charset="utf-8">
<title>Smoothie Menu</title>
<link href="https://fonts.googleapis.com/css2?family=Lobster&family=Dosis:wght@500;600&family=Catamaran:wght@400;500&display=swap" rel="stylesheet">
<style>
  :root {
    --bg: #f2f2f1;
    --purple: #7a52a3;
    --green: #6cbd4e;
    --pink: #e0357b;
    --orange: #f5921e;
    --navy: #3556a3;
    --ink: #2b2b2b;
    --tag: #4a4a4a;
    --dots: #555;
  }
  * { margin: 0; padding: 0; box-sizing: border-box; }
  html, body { width: 1200px; height: 848px; overflow: hidden; }
  body { background: var(--bg); font-family: "Catamaran", sans-serif; color: var(--ink); }
  .menu { position: relative; width: 1200px; height: 848px; background: linear-gradient(180deg, #f6f6f5, #ececeb); overflow: hidden; }
  .abs { position: absolute; }

  .section-title { position: absolute; font-family: "Lobster", cursive; font-weight: 400; font-size: 47px; line-height: 1; }
  .rule { position: absolute; border-top: 3px dotted var(--dots); height: 0; }

  .price-badge { position: absolute; width: 92px; height: 92px; border-radius: 50%; color: #fff;
    font-family: "Dosis", sans-serif; font-weight: 600; font-size: 16px; line-height: 1.2;
    display: flex; flex-direction: column; justify-content: center; align-items: center; }
  .price-badge.purple { background: var(--purple); }
  .price-badge.green { background: var(--green); }

  .item { position: absolute; }
  .item-name { font-family: "Lobster", cursive; font-size: 26px; line-height: 1.05; }
  .item-tags { font-family: "Dosis", sans-serif; font-weight: 600; font-size: 17px; color: var(--tag); }
  .item-desc { font-size: 13px; line-height: 1.45; margin-top: 3px; }
  .superfruit .item-name { color: var(--purple); }
  .vegan .item-name { color: var(--green); }

  .photo { position: absolute; }

  .yoghurt-box { position: absolute; left: 40px; top: 508px; width: 668px; height: 298px; border: 2px dotted var(--pink); }
  .block-title { position: absolute; font-family: "Lobster", cursive; font-size: 44px; line-height: 1; }
  .block-sub { position: absolute; font-family: "Dosis", sans-serif; font-weight: 600; font-size: 16px; color: var(--tag); }
  .price-row { position: absolute; display: flex; justify-content: space-between; font-family: "Dosis", sans-serif; font-weight: 500; font-size: 16px; color: var(--ink); }
  .price-row b { font-weight: 600; }
  .pink b { color: var(--pink); }
  .orange b { color: var(--orange); }
  .mini-rule { position: absolute; border-top: 2px dotted var(--dots); }

  .extras-title { position: absolute; left: 905px; top: 503px; font-family: "Lobster", cursive; font-size: 42px; color: var(--navy); }
  .extras-list { position: absolute; left: 905px; top: 578px; width: 255px; list-style: none; }
  .extras-list li { display: flex; justify-content: space-between; align-items: baseline; height: 40.5px;
    font-family: "Lobster", cursive; font-size: 26px; color: var(--navy); }
  .extras-list .cost { font-size: 20px; color: #333; }
</style>
</head>
<body>
<main class="menu">

  <!-- SuperFruit Smoothies -->
  <section class="superfruit">
    <h2 class="section-title" style="left:40px;top:36px;color:var(--purple)">SuperFruit Smoothies</h2>
    <div class="rule" style="left:40px;top:97px;width:520px"></div>
    <div class="price-badge purple" style="left:488px;top:38px"><span>Reg $8.95</span><span>Large $9.95</span></div>

    <div class="item" style="left:40px;top:115px;width:420px">
      <div><span class="item-name">Tropical Tonic</span> <span class="item-tags">(Muscle, Weight Loss, Vitality)</span></div>
      <p class="item-desc">Vanilla Protein, Passionfruit, Almonds, Mango, Avocado,<br>Manuka Honey, Chia Seeds, Coconut Water, Ice</p>
    </div>
    <div class="item" style="left:40px;top:198px;width:430px">
      <div><span class="item-name">Banana Bliss</span> <span class="item-tags">(Favourite, Muscle, Weight Loss)</span></div>
      <p class="item-desc">Banana Protein, Banana, Cacao Nibs, Manuka Honey, Chia Seeds,<br>Walnuts, Cinnamon, Chia Seeds, Water, Ice</p>
    </div>
    <div class="item" style="left:40px;top:283px;width:430px">
      <div><span class="item-name">Berry Sweet</span> <span class="item-tags">(Favourite, Muscle, Weight Loss)</span></div>
      <p class="item-desc">Strawberry Protein, Mixed Berries, Acai Powder, Goji Berries,<br>Cranberries, Shredded Coconut, Water, Ice</p>
    </div>
    <div class="item" style="left:40px;top:366px;width:520px">
      <div><span class="item-name">Peach Pick-Me-Up</span> <span class="item-tags">(Muscle, Weight Loss, Vitality)</span></div>
      <p class="item-desc">Vanilla Protein, Peach, Banana, Kale, Pear, Almonds, Chia Seeds, Coconut Water, Ice</p>
    </div>
    <div class="item" style="left:40px;top:429px;width:540px">
      <div><span class="item-name">Mango Madness</span> <span class="item-tags">(Favourite, Muscle, Weight Loss, Vitality)</span></div>
      <p class="item-desc">Vanilla Protein, Mango, Almond Flakes, Manuka Honey, Ice, Chia Seeds, Water, Ice</p>
    </div>

    <div class="photo" role="img" aria-label="Two smoothie cups, one mango yellow and one berry purple, with fresh berries"
      style="left:445px;top:140px;width:205px;height:240px;border-radius:14px;background:linear-gradient(100deg,#f3dc8a 0%,#f0d27a 45%,#6d3f86 55%,#583172 100%)"></div>
  </section>

  <!-- Vegan Smoothies -->
  <section class="vegan">
    <h2 class="section-title" style="left:658px;top:36px;color:var(--green)">Vegan Smoothies</h2>
    <div class="rule" style="left:658px;top:97px;width:420px"></div>
    <div class="price-badge green" style="left:1066px;top:38px"><span>Reg $8.95</span><span>Large $9.95</span></div>

    <div class="item" style="left:658px;top:115px;width:510px">
      <div><span class="item-name">Acai</span> <span class="item-tags">(Vitality, Weight Loss, Dairy Free, Gluten Free)</span></div>
      <p class="item-desc">Acai Powder, Banana, Chia Seeds, Goji Berries, Cranberries, Coconut Water, Ice</p>
    </div>
    <div class="item" style="left:658px;top:178px;width:510px">
      <div><span class="item-name">Energiser</span> <span class="item-tags">(Vitality, Weight Loss, Dairy Free, Gluten Free)</span></div>
      <p class="item-desc">Raw Energy Powder (traditional herbs, slow-release ancient seeds, and concentrated sea minerals), Acai Powder, Blueberries, Avocado, Chia Seeds, Coconut Water, Ice</p>
    </div>
    <div class="item" style="left:658px;top:262px;width:510px">
      <div><span class="item-name">Complete Biotic</span> <span class="item-tags" style="letter-spacing:-0.3px">(Vitality, Weight Loss, Dairy Free, Gluten Free)</span></div>
      <p class="item-desc">Raw Pre-Probiotic Powder, Mango, Chia Seeds, Almond Flakes, Coconut Water, Ice</p>
    </div>
    <div class="item" style="left:658px;top:326px;width:510px">
      <div><span class="item-name">Vegan Vigor</span> <span class="item-tags">(Favourite, Muscle, Weight Loss, Vitality, Dairy Free, Gluten Free)</span></div>
      <p class="item-desc">Vegetable Protein, Blueberries, Banana, Cinnamon, Walnuts, Chia Seeds, Antioxidant Mix (pomegranate, maqui, acai, elderflower, green tea powder), Coconut Water, Ice</p>
    </div>
  </section>

  <!-- Frozen Yoghurt & Protein Pancakes -->
  <section class="yoghurt-pancakes">
    <div class="yoghurt-box"></div>
    <div class="photo" role="img" aria-label="Stack of protein pancakes with strawberries, banana slices and frozen yoghurt cups with blueberries"
      style="left:42px;top:500px;width:258px;height:318px;border-radius:16px;background:linear-gradient(170deg,#e9c79a 0%,#f0dcc0 45%,#f7f5ef 70%,#8fd0cf 100%)"></div>

    <h2 class="block-title" style="left:312px;top:530px;color:var(--pink)">Frozen Yoghurt</h2>
    <p class="block-sub" style="left:312px;top:576px">(Up to 3 toppings - extra toppings $0.50 each)</p>
    <div class="price-row pink" style="left:312px;top:616px;width:364px">
      <span>Small <b>$4.50</b></span><span>Medium <b>$6.00</b></span><span>Large <b>$7.50</b></span>
    </div>
    <div class="mini-rule" style="left:312px;top:662px;width:364px"></div>

    <h2 class="block-title" style="left:312px;top:688px;color:var(--orange)">Protein Pancakes</h2>
    <p class="block-sub" style="left:312px;top:736px">(Available in Chocolate, Strawberry, Banana)</p>
    <div class="price-row orange" style="left:312px;top:773px;width:364px">
      <span>3 Stack <b>$6.95</b></span><span>5 Stack <b>$8.45</b></span><span>Protein Pocket <b>$3.50</b></span>
    </div>
  </section>

  <!-- Utensils photo -->
  <div class="photo" role="img" aria-label="Bamboo fork and spoon"
    style="left:752px;top:458px;width:130px;height:340px;border-radius:40px;background:linear-gradient(90deg,#d8b27c,#c99b5e)"></div>

  <!-- Food & Extras -->
  <section class="extras">
    <h2 class="extras-title">Food &amp; Extra’s</h2>
    <div class="rule" style="left:905px;top:565px;width:255px"></div>
    <ul class="extras-list">
      <li><span>Acai Bowl</span><span class="cost">$9.95</span></li>
      <li><span>Protein Balls</span><span class="cost">$2</span></li>
      <li><span>Vantor Bars</span><span class="cost">$4.50</span></li>
      <li><span>Lumo-Leaf Tea</span><span class="cost">$3.95</span></li>
      <li><span>Bottled Water</span><span class="cost">$2.45</span></li>
      <li><span>Coconut Water</span><span class="cost">$3.30</span></li>
    </ul>
  </section>

</main>
</body>
</html>
```